Lantern Lens Guild

Its a flyer to promote free seminars for alternative photographic techniques. We need to include brief information about the two people who are giving the seminar, Gavin Thorpe and Alan Brook and a short description of the methods used. Photo gravure; Gum bichromate, carbon printing. The Seminars are FREE, and will be on march 14th and 15th at Lantern Guild Studios, 27 Marlow Road Kingston upon Thames KT2 4RJ we would like to add a things saying 'please let us know you are coming on 'lanternlensguild@examplemail.net or via our facebook page (also called lantern lenses Guild) if we could add a facebook logo thing
Seminars will be 2 hours long 12 -2 pm

Strap line something like " Discover the creativity of early photographic processes'

And we need the fliers by Saturday!

```html
<!DOCTYPE html>
<html lang="en">
<head>
<meta charset="UTF-8">
<title>Discover the Creativity of Early Photographic Processes – Lantern Lens Guild</title>
<link href="https://fonts.googleapis.com/css2?family=Josefin+Sans:ital,wght@0,400;0,600;0,700;1,400&display=swap" rel="stylesheet">
<style>
  :root {
    --ink: #000000;
    --paper: #ffffff;
    --soft-text: #e6e6e6;
    --muted-text: #bdbdbd;
    --rule: #8a8a8a;
    --panel-top: #2b2b2b;
    --panel-mid: #141414;
    --hero-dark: #0c0b0a;
    --hero-warm: #4a3a2e;
    --ember-top: #8a5c12;
    --ember-bottom: #5a1c06;
    --icon-disc: #3a3a3a;
    --font-main: "Josefin Sans", "Century Gothic", sans-serif;
  }
  * { margin: 0; padding: 0; box-sizing: border-box; }
  html, body { width: 849px; height: 1200px; overflow: hidden; background: var(--ink); }
  .flyer {
    position: relative; width: 849px; height: 1200px; overflow: hidden;
    font-family: var(--font-main); color: var(--paper);
    background: radial-gradient(ellipse 700px 520px at 20% 68%, var(--panel-top) 0%, var(--panel-mid) 55%, var(--ink) 100%);
  }
  .hero-photo {
    position: absolute; left: 0; top: 0; width: 849px; height: 456px;
    background:
      radial-gradient(circle 150px at 690px 170px, #3a3a3e 0%, #16161a 60%, transparent 100%),
      linear-gradient(100deg, #6e6052 0%, var(--hero-warm) 28%, #231d18 50%, var(--hero-dark) 100%);
  }
  .headline {
    position: absolute; left: 38px; top: 96px;
    font-weight: 700; text-transform: uppercase; line-height: 1; letter-spacing: 0;
  }
  .headline span { display: block; }
  .headline .l1 { font-size: 46px; }
  .headline .l2 { font-size: 45px; margin-top: 6px; }
  .headline .l3 { font-size: 40px; margin-top: 8px; }
  .headline .l4 { font-size: 50px; margin-top: 8px; }
  .headline .l5 { font-size: 44px; margin-top: 8px; }
  .headline small { font-size: 0.7em; }
  .photo-strip { position: absolute; left: 0; top: 456px; width: 849px; height: 166px; }
  .ember { position: absolute; left: 0; top: 0; width: 849px; height: 1200px; pointer-events: none; }
  .speakers {
    position: absolute; left: 46px; top: 652px;
    font-size: 30px; font-weight: 600; text-transform: uppercase; letter-spacing: 0.3px;
  }
  .speakers-bio {
    position: absolute; left: 47px; top: 690px;
    font-size: 15px; color: var(--muted-text);
  }
  .divider { position: absolute; left: 44px; top: 716px; width: 534px; height: 1px; background: var(--rule); }
  .methods-intro { position: absolute; left: 47px; top: 745px; font-size: 18px; color: var(--soft-text); }
  .methods { position: absolute; left: 50px; top: 792px; list-style: none; font-size: 16px; color: var(--soft-text); }
  .methods li { position: relative; padding-left: 21px; height: 30.5px; }
  .methods li::before {
    content: ""; position: absolute; left: 0; top: 3px; width: 9px; height: 9px;
    border: 1.5px solid var(--soft-text); border-radius: 50%;
    background: radial-gradient(circle, var(--soft-text) 0 2px, transparent 2.5px);
  }
  .event { position: absolute; left: 46px; top: 916px; color: var(--paper); }
  .event .when { font-size: 20px; }
  .event .when b { font-weight: 600; }
  .event .venue { font-size: 23px; margin-top: 10px; }
  .event .address { font-size: 19px; margin-top: 6px; }
  .rsvp { position: absolute; left: 46px; top: 1040px; font-size: 20px; font-style: italic; }
  .contact { position: absolute; left: 46px; font-size: 20px; font-style: italic; display: flex; align-items: center; }
  .contact .dot { width: 34px; height: 34px; border-radius: 50%; background: var(--icon-disc); margin-right: 17px; flex: none; }
  .contact.email { top: 1087px; }
  .contact.page { top: 1134px; }
</style>
</head>
<body>
<main class="flyer">
  <div class="hero-photo" role="img" aria-label="Dark still life of a camera with a lens beside a sheet of patterned print paper"></div>

  <h1 class="headline">
    <span class="l1">Discover</span>
    <span class="l2"><small>The</small> Creativity</span>
    <span class="l3"><small>of</small> Early</span>
    <span class="l4">Photographic</span>
    <span class="l5">Processes</span>
  </h1>

  <svg class="photo-strip" viewBox="0 0 849 166">
    <defs>
      <linearGradient id="tone-town" x1="0" y1="0" x2="0" y2="1">
        <stop offset="0" stop-color="#9a8a6c"/><stop offset="1" stop-color="#4e4230"/>
      </linearGradient>
      <linearGradient id="tone-woods" x1="0" y1="0" x2="0" y2="1">
        <stop offset="0" stop-color="#7d8a96"/><stop offset="1" stop-color="#2c3844"/>
      </linearGradient>
      <linearGradient id="tone-dance" x1="0" y1="0" x2="1" y2="1">
        <stop offset="0" stop-color="#6a5048"/><stop offset="1" stop-color="#3a2a26"/>
      </linearGradient>
      <linearGradient id="tone-portrait" x1="0" y1="0" x2="1" y2="0">
        <stop offset="0" stop-color="#1a1a1a"/><stop offset="1" stop-color="#3c3c3c"/>
      </linearGradient>
    </defs>
    <rect width="849" height="166" fill="var(--paper)"/>
    <polygon role="img" aria-label="Sepia print of a town skyline at dusk" points="0,2 202,2 143,166 0,166" fill="url(#tone-town)"/>
    <polygon role="img" aria-label="Blue-toned print of bare trees reflected in water" points="207,2 438,2 379,166 148,166" fill="url(#tone-woods)"/>
    <polygon role="img" aria-label="Warm-toned print of a dancer in a flowing skirt" points="443,2 678,2 620,166 384,166" fill="url(#tone-dance)"/>
    <polygon role="img" aria-label="Black and white close-up portrait" points="683,2 849,2 849,166 625,166" fill="url(#tone-portrait)"/>
  </svg>

  <svg class="ember" viewBox="0 0 849 1200" aria-hidden="true">
    <defs>
      <linearGradient id="ember-fill" x1="0" y1="0" x2="0" y2="1">
        <stop offset="0" stop-color="var(--ember-top)"/><stop offset="1" stop-color="var(--ember-bottom)"/>
      </linearGradient>
    </defs>
    <polygon points="849,750 849,1200 664,1200" fill="url(#ember-fill)"/>
  </svg>

  <h2 class="speakers">Gavin Thorpe and Alan Brook</h2>
  <p class="speakers-bio">Printmakers and tutors in historic photographic print processes</p>
  <div class="divider"></div>

  <p class="methods-intro">Short description of the methods used in</p>
  <ul class="methods">
    <li>Photo Gravure</li>
    <li>Gum Bichromate</li>
    <li>Carbon Printing</li>
  </ul>

  <section class="event">
    <p class="when">FREE 2-HOUR SEMINAR, On <b>march 14th</b> and <b>15th</b>, <b>12 – 2 pm</b> at</p>
    <p class="venue">Lantern Guild Studios,</p>
    <p class="address">27 Marlow Road Kingston upon Thames KT2 4RJ</p>
  </section>

  <p class="rsvp">Please let us know you are coming on</p>
  <p class="contact email"><span class="dot"></span>lanternlensguild@examplemail.net</p>
  <p class="contact page"><span class="dot"></span>lantern lenses Guild</p>
</main>
</body>
</html>
```